Bright Meadow Counseling Business Card design with a visually interesting use of Space

I need business cards that are luxurious and give a peaceful, calm vibe. I also had some letterhead designed, and i like the look of it also, it's attached with the logo design for reference/ ideas but feel free to be creative.

Target Market(s)

High end luxurious client who needs counseling

Industry/Entity Type

Marriage and Family Therapy

Contact Information for Business Card

Mira Kowalczyk MS LMFT/ or Toby Hallett address 4150 Larkin Suite 600

Font styles to use
Sans Serif

Colors
0054AA
0677BA
7BADD7
CADEEF
E8F1F8
0094D4
00A9DD
6FCCEA
C7EBF8
E9F6FB
A7469A
B969AE
D3A5CF
EDDBEB
F8F0F9
6B429C
8869AF
B7A5CE
E3DAEB
F3F0F8

Requirements
Must have
• Logo and color scheme but be simple modern and luxurious
Nice to have
• I'd like to incorporate some elelmets from the logo and letterhead into a simple modern card

```html
<!DOCTYPE html>
<html lang="en">
<head>
<meta charset="utf-8">
<title>Bright Meadow Counseling – Business Card</title>
<link rel="stylesheet" href="https://fonts.googleapis.com/css2?family=Poppins:wght@300;400;600&display=swap">
<style>
  :root {
    --bg: #2b2b2d;
    --card: #ffffff;
    --ink: #111111;
    --text-grey: #4a4a4a;
    --teal: #2fb3b3;
    --teal-dark: #1f7f86;
    --magenta: #a7469a;
    --violet: #8155ab;
    --mark: #8869af;
  }
  * { box-sizing: border-box; margin: 0; padding: 0; }
  html, body { width: 1200px; height: 1024px; overflow: hidden; }
  body {
    background: var(--bg);
    font-family: "Poppins", sans-serif;
    position: relative;
  }
  .card {
    position: absolute;
    left: 190px;
    width: 820px;
    height: 460px;
    background: var(--card);
    box-shadow: 0 10px 30px rgba(0,0,0,.45);
    overflow: hidden;
  }
  .card--front { top: 34px; }
  .card--back { top: 530px; }

  .brand {
    position: absolute;
    display: flex;
    align-items: flex-start;
    gap: 18px;
    color: var(--ink);
    font-weight: 300;
  }
  .brand__dot {
    width: 30px; height: 30px;
    border-radius: 50%;
    background: var(--mark);
    margin-top: 16px;
    flex: none;
  }
  .brand__text { display: flex; flex-direction: column; line-height: 1; }
  .brand__name { font-size: 56px; letter-spacing: 1px; }
  .brand__tag {
    font-size: 26px;
    letter-spacing: 9px;
    align-self: flex-end;
    margin-top: 6px;
  }
  .card--front .brand { left: 180px; top: 170px; }
  .card--back .brand { left: 150px; top: 70px; }

  .rule {
    position: absolute;
    bottom: 46px;
    left: 220px;
    right: 70px;
    height: 4px;
    display: flex;
    gap: 4px;
  }
  .rule span { height: 100%; }
  .rule .seg-violet { flex: 22; background: var(--violet); }
  .rule .seg-magenta { flex: 21; background: var(--magenta); }
  .rule .seg-teal { flex: 20; background: var(--teal); }

  .address {
    position: absolute;
    right: 70px;
    top: 200px;
    text-align: right;
    font-style: normal;
    font-size: 18px;
    line-height: 1.35;
    color: var(--text-grey);
  }
  .address__web {
    font-weight: 600;
    color: var(--teal-dark);
    font-size: 19px;
    letter-spacing: .3px;
  }

  .contact {
    position: absolute;
    left: 220px;
    bottom: 62px;
    list-style: none;
    font-size: 19px;
    line-height: 1.35;
    color: var(--text-grey);
  }
  .contact li { display: flex; align-items: center; gap: 10px; }
  .contact svg { width: 16px; height: 16px; fill: var(--teal-dark); flex: none; }
</style>
</head>
<body>

  <section class="card card--front" aria-label="Card front">
    <div class="brand">
      <span class="brand__dot"></span>
      <div class="brand__text">
        <span class="brand__name">Bright Meadow</span>
        <span class="brand__tag">Counseling</span>
      </div>
    </div>
    <div class="rule"><span class="seg-violet"></span><span class="seg-magenta"></span><span class="seg-magenta"></span><span class="seg-teal"></span></div>
  </section>

  <section class="card card--back" aria-label="Card back">
    <div class="brand">
      <span class="brand__dot"></span>
      <div class="brand__text">
        <span class="brand__name">Bright Meadow</span>
        <span class="brand__tag">Counseling</span>
      </div>
    </div>

    <address class="address">
      4150 Larkin Suite 600<br>
      Juneau, Alaska 99801<br>
      <span class="address__web">www.brightmeadowcounsel.com</span>
    </address>

    <ul class="contact">
      <li>
        <svg viewBox="0 0 16 16" aria-hidden="true"><path d="M3.2 1.5l2.3-.5 1.4 3.3-1.6 1.2a8 8 0 0 0 4.2 4.2l1.2-1.6 3.3 1.4-.5 2.3c-.2.8-.9 1.2-1.7 1.1C6.6 12.4 3.6 9.4 2.1 3.2 2 2.4 2.4 1.7 3.2 1.5z"/></svg>
        555-214-7730
      </li>
      <li>
        <svg viewBox="0 0 16 16" aria-hidden="true"><path d="M4 1h6l2 2v3H4z M1 6h14v7h-2v2H3v-2H1z M5 10v3h6v-3z"/></svg>
        555-214-7731
      </li>
      <li>
        <svg viewBox="0 0 16 16" aria-hidden="true"><path d="M1 3h14v10H1z M2.5 4.2L8 8.6l5.5-4.4v-.2h-11z" fill-rule="evenodd"/></svg>
        info@brightmeadowcounsel.com
      </li>
    </ul>

    <div class="rule"><span class="seg-violet"></span><span class="seg-magenta"></span><span class="seg-magenta"></span><span class="seg-teal"></span></div>
  </section>

</body>
</html>
```